Tobias Wrenfield - Cinematographer

NEED:
I'm looking for a sleek, professional, modern business card that will give give the recipient the impression that they can trust their production will go smoothly by hiring me. I will bring creativity and knowledge to their shoot, so that we can create powerful images.
I am looking for a card with a strong style and design ethos that could be expanded to a website and a full visual/graphic/design entity for me.
ABOUT ME:
I am a mid-twenties cinematographer, I work on music video, narrative short, commercial, and corporate projects. I blend the science and artistry of cameras and filmmaking to tell a story. I'm an artist, a technician, and a manager.
DESIGN:
I like sleek, simple design. Black, dark grays, white, dark navy, steel blues, I love cyan, but also cyan and red. I am not a fan of earthy tones. I generally prefer modern, san-serif fonts over serifs. My old logo was based on an aperture, a multi-blade device at the back of a lens that controls how much light passes through, but I made it with so many colors, that it doesn't necessarily lend itself to a specific color-scheme or design ethos. I liked that the aperture design provided a sense of the technical requirements of my job. I'm a fan of matte business cards, but am open to plenty of specialty print processes to make an outstanding card.
ATTACHED FILES:
My Old Rainbox Aperture Logo, plus a few designs I've tried playing around with, but am not tied to. I AM OPEN TO NEW DESIGNS, DO NOT FEEL TIED TO THIS.
**I've pulled my old logo down from the attached files, and instead attached other business cards I like, so as not to mislead you where I would like to go.
INFO:
Name: Tobias Wrenfield
Job: Cinematographer
Email: tkwrenfield@quillbox.example
Phone: 503.618.2907
Website: tobiaswrenfield.example
Updates
I'm adding some images of other cards that I like, and removing my old logo, since I'm looking for something new, and don't want that old logo to push anyone a certain direction.

```html
<!DOCTYPE html>
<html lang="en">
<head>
<meta charset="utf-8">
<title>Tobias Wrenfield – Cinematographer – Business Card</title>
<link rel="stylesheet" href="https://fonts.googleapis.com/css2?family=Yanone+Kaffeesatz:wght@200;300&family=Questrial&display=swap">
<style>
  :root {
    --backdrop: #72c9c0;
    --card: #ffffff;
    --ink: #2a2a2a;
    --frame-line: #cfe9e6;
    --coral: #f2876c;
    --mint: #a9ddd8;
  }
  * { box-sizing: border-box; margin: 0; padding: 0; }
  html, body {
    width: 1200px; height: 900px; overflow: hidden;
    background: var(--backdrop);
  }
  .stage { position: relative; width: 1200px; height: 900px; }
  .card {
    position: absolute; top: 117px;
    width: 411px; height: 666px;
    background: var(--card);
  }
  .card--front { left: 150px; }
  .card--back { left: 661px; }
  .card__frame { position: absolute; inset: 0; }
  .mark-name {
    position: absolute; left: 0; right: 0; top: 205px;
    text-align: center;
    font-family: "Yanone Kaffeesatz", sans-serif; font-weight: 300;
    font-size: 78px; line-height: 0.95; letter-spacing: 3px;
    color: var(--coral); text-transform: uppercase;
  }
  .identity {
    position: absolute; left: 0; right: 0; top: 498px;
    text-align: center; color: var(--ink);
  }
  .identity__name {
    font-family: "Yanone Kaffeesatz", sans-serif; font-weight: 200;
    font-size: 62px; line-height: 1; letter-spacing: 2px;
    text-transform: uppercase;
  }
  .identity__role {
    font-family: "Questrial", sans-serif;
    font-size: 25px; line-height: 1; letter-spacing: 1.5px;
    text-transform: uppercase; margin-top: 2px;
  }
  .contact {
    position: absolute; left: 0; right: 0; text-align: center;
    font-family: "Yanone Kaffeesatz", sans-serif; font-weight: 200;
    color: var(--ink); text-transform: uppercase;
  }
  .contact--phone { top: 98px; font-size: 52px; letter-spacing: 1px; }
  .contact--web { top: 498px; font-size: 32px; letter-spacing: 0.5px; }
  .contact--mail { top: 546px; font-size: 32px; letter-spacing: 0.5px; }
  .target { position: absolute; left: 0; top: 0; }
  .target-name {
    position: absolute; left: 0; right: 0; top: 318px;
    text-align: center;
    font-family: "Yanone Kaffeesatz", sans-serif; font-weight: 300;
    font-size: 26px; line-height: 1; letter-spacing: 1px;
    color: var(--coral); text-transform: uppercase;
  }
</style>
</head>
<body>
<main class="stage">
  <section class="card card--front" aria-label="Card front">
    <svg class="card__frame" width="411" height="666" viewBox="0 0 411 666" aria-hidden="true">
      <g fill="none" stroke="var(--frame-line)" stroke-width="1.5">
        <path d="M27 80 V27 H82"/>
        <path d="M329 27 H384 V80"/>
        <path d="M27 585 V639 H82"/>
        <path d="M329 639 H384 V585"/>
      </g>
    </svg>
    <div class="mark-name">Tobias<br>Wrenfield</div>
    <div class="identity">
      <h1 class="identity__name">Tobias Wrenfield</h1>
      <p class="identity__role">Cinematographer</p>
    </div>
  </section>

  <section class="card card--back" aria-label="Card back">
    <svg class="card__frame" width="411" height="666" viewBox="0 0 411 666" aria-hidden="true">
      <g fill="none" stroke="var(--frame-line)" stroke-width="1.5">
        <path d="M27 80 V27 H82"/>
        <path d="M329 27 H384 V80"/>
        <path d="M27 585 V639 H82"/>
        <path d="M329 639 H384 V585"/>
      </g>
      <g class="target" fill="none" stroke="var(--frame-line)" stroke-width="1.5">
        <circle cx="207" cy="333" r="97"/>
        <circle cx="207" cy="333" r="77"/>
        <path d="M110 333 H304"/>
        <path d="M207 236 V430"/>
      </g>
    </svg>
    <p class="contact contact--phone">503.618.2907</p>
    <div class="target-name">Wrenfield</div>
    <p class="contact contact--web">tobiaswrenfield.example</p>
    <p class="contact contact--mail">tkwrenfield@quillbox.example</p>
  </section>
</main>
</body>
</html>
```